Brevo Handset Cradle cardboard sleeve

Card-board sleeve packaging design.
Dimensions: length 87mm, Width 65mm, height 26mm (see product picture)

'Green png logo' prominent on the front side however colour is negotiable.

And the strapblurb4 on the back, landscape. foot logo in the position shown. Font open to suggestions.

On the side of packaging should state 'Brevo can hold every smartphone'.

Overall design should be......funny, funky vibe, in keeping with the blurb for the back. Perhaps vibrant or Primary colours as actual PRODUCT WILL BE BLACK NOT YELLOW.

Reason: not enough designs yet :(

Target Market(s)

all smartphone users

But will be used on Bikes, Shopping Karts/Trolleys, Baby buggies/Strollers

Industry/Entity Type

Product

Colors

Designer to choose colors to be used in the design.

Requirements
Must have
• Fun and eye-catching feel
Nice to have
• unique and progressive design style

```html
<!DOCTYPE html>
<html lang="en">
<head>
<meta charset="utf-8">
<title>Mitzo Handset Cradle – sleeve panels</title>
<link rel="stylesheet" href="https://fonts.googleapis.com/css2?family=Zilla+Slab:wght@400;700&display=swap">
<style>
  :root {
    --backdrop: #2b2c2e;
    --sleeve-light: #86c440;
    --sleeve-mid: #72b236;
    --sleeve-deep: #5e9a2a;
    --ink: #0d0f0a;
  }
  * { margin: 0; padding: 0; box-sizing: border-box; }
  html, body {
    width: 1200px; height: 900px; overflow: hidden;
    background: var(--backdrop);
  }
  .canvas { position: relative; width: 1200px; height: 900px; }
  .panel {
    position: absolute;
    width: 269px; height: 380px;
    color: var(--ink);
    font-family: "Zilla Slab", Georgia, serif;
    background: linear-gradient(160deg, var(--sleeve-light) 0%, var(--sleeve-mid) 55%, var(--sleeve-deep) 100%);
  }
  .panel-front { left: 272px; top: 318px; }
  .panel-back { left: 670px; top: 192px; }

  .brand-mark {
    position: absolute; left: 0; right: 0;
    display: flex; flex-direction: column; align-items: center;
  }
  .brand-dot { border-radius: 50%; background: var(--ink); }
  .brand-name { font-weight: 700; line-height: 1; letter-spacing: 1px; }

  .panel-front .brand-mark { top: 121px; }
  .panel-front .brand-dot { width: 98px; height: 98px; }
  .panel-front .brand-name { font-size: 46px; margin-top: 4px; }

  .panel-back .brand-mark { top: 24px; }
  .panel-back .brand-dot { width: 112px; height: 112px; }
  .panel-back .brand-name { font-size: 24px; margin-top: 6px; }

  .blurb-lead {
    position: absolute; left: 30px; top: 188px; width: 212px;
    font-size: 12px; line-height: 14px;
  }
  .blurb-detail {
    position: absolute; left: 74px; top: 243px; width: 180px;
    font-size: 8.5px; line-height: 10.5px;
  }
  .blurb-call {
    position: absolute; left: 20px; right: 20px; top: 305px;
    text-align: center; font-size: 12px; line-height: 14px;
  }
  .blurb-call strong { font-weight: 700; }
</style>
</head>
<body>
<main class="canvas">
  <section class="panel panel-front" aria-label="Sleeve front">
    <div class="brand-mark">
      <span class="brand-dot"></span>
      <span class="brand-name">Mitzo</span>
    </div>
  </section>

  <section class="panel panel-back" aria-label="Sleeve back">
    <div class="brand-mark">
      <span class="brand-dot"></span>
      <span class="brand-name">Mitzo</span>
    </div>
    <p class="blurb-lead">When you put your Sleek new smartphone down, you need it in safe hands.</p>
    <p class="blurb-detail">There’s lots of fancy gadgets out there but let’s face it, when you want ‘non-slip’ and ‘sticky’ there nothing like good old fashioned rubber.</p>
    <p class="blurb-call">Let Mitzo get its <strong>Sticky Little Mits</strong> on your smartphone!</p>
  </section>
</main>
</body>
</html>
```